50 Puffira Mouthpieces box design for breathalyser device

Theis is a box design stencil in the files to go off.
Please feel free to use your own creativeness for the design.
Front design should have "50 mouthpieces" and the Puffira logo. Please no pictures of breathalysers on the front.

Please include below statements on back of box.
*50 Puffira Mouthpieces
*Premium Hygenic Plastic
*Disposable
*CE Approved
puffira.com.au

Target Market(s)

Contruction sites, medical centres,

Colors
EB3D1F
EC4F4E
F09395
F8D3D4
FCEDEE

Requirements
Must have
• I like the colour schemes of the puffira box design already. So mostly black, and red and white.

```html
<!DOCTYPE html>
<html lang="en">
<head>
<meta charset="utf-8">
<title>Puffira Mouthpieces – 50 Pack Box</title>
<link href="https://fonts.googleapis.com/css2?family=Poppins:wght@400;500;600;800&display=swap" rel="stylesheet">
<style>
  :root {
    --black: #000000;
    --panel: #0a0a0a;
    --white: #ffffff;
    --red: #eb3d1f;
    --red-deep: #e8000f;
    --red-dark: #7a0008;
    --grey: #8a8a8a;
    --bg: #f2f2f2;
  }
  * { box-sizing: border-box; margin: 0; padding: 0; }
  html, body { width: 1200px; height: 1000px; overflow: hidden; }
  body {
    background: var(--bg);
    font-family: "Poppins", sans-serif;
    color: var(--white);
    position: relative;
  }
  .panel {
    position: absolute;
    top: 70px;
    width: 460px;
    height: 860px;
    background: var(--panel);
    overflow: hidden;
  }
  .panel--front { left: 100px; }
  .panel--back { left: 640px; }

  .hang-tab {
    position: relative;
    height: 140px;
    background: var(--black);
    border-bottom: 2px solid #2a2a2a;
  }
  .hang-hole {
    position: absolute;
    left: 50%;
    top: 28px;
    width: 96px;
    height: 26px;
    margin-left: -48px;
    background: var(--white);
    border-radius: 48px 48px 6px 6px;
  }
  .tab-brand {
    position: absolute;
    left: 0; right: 0;
    top: 68px;
    display: flex;
    justify-content: center;
    align-items: center;
    gap: 22px;
  }
  .brand {
    display: inline-flex;
    flex-direction: column;
    align-items: flex-end;
  }
  .brand__name {
    font-weight: 800;
    color: var(--white);
    letter-spacing: 1px;
    line-height: 1;
  }
  .brand__url {
    font-weight: 400;
    color: var(--white);
    line-height: 1.2;
  }
  .brand--small .brand__name { font-size: 28px; }
  .brand--small .brand__url { font-size: 11px; }
  .brand--large .brand__name { font-size: 44px; }
  .brand--large .brand__url { font-size: 16px; }
  .count-badge {
    display: flex;
    align-items: center;
    gap: 6px;
  }
  .count-badge__num {
    font-weight: 600;
    font-size: 22px;
    border: 2px solid var(--red);
    border-radius: 6px;
    padding: 0 6px;
    line-height: 34px;
  }
  .count-badge__icon {
    width: 36px;
    height: 40px;
    background: linear-gradient(90deg, #3a0003, var(--red-deep), #3a0003);
    border-radius: 4px;
  }

  .body {
    position: relative;
    height: 600px;
    background: linear-gradient(90deg, #2a2a2a 0%, #0a0a0a 35%, #000 100%);
  }
  .front-title {
    position: absolute;
    top: 72px;
    left: 0; right: 0;
    text-align: center;
  }
  .front-title .brand { margin-left: 40px; }
  .product-label {
    margin-top: 30px;
    font-size: 22px;
    font-weight: 500;
    letter-spacing: 3px;
  }
  .mouthpiece-art {
    position: absolute;
    right: 40px;
    bottom: 0;
    width: 170px;
    height: 270px;
    background: linear-gradient(180deg, #3a0003, #8a0010 60%, #2a0002);
    border-radius: 10px;
  }

  .pack-band {
    position: absolute;
    left: 0; right: 0; bottom: 0;
    height: 120px;
  }
  .pack-band svg { position: absolute; inset: 0; }
  .pack-band__text {
    position: absolute;
    left: 36px;
    bottom: 20px;
    display: flex;
    align-items: baseline;
    gap: 12px;
  }
  .pack-band__num { font-size: 66px; font-weight: 800; line-height: 1; }
  .pack-band__word { font-size: 20px; font-weight: 500; letter-spacing: 4px; }
  .pack-band__url {
    position: absolute;
    right: 30px;
    bottom: 30px;
    font-size: 28px;
    font-weight: 500;
  }

  .back-content { padding: 36px 40px 0; }
  .back-heading { font-size: 22px; font-weight: 500; text-align: center; }
  .feature-list { list-style: none; margin-top: 24px; }
  .feature-list li {
    display: flex;
    align-items: center;
    gap: 12px;
    font-size: 17px;
    font-weight: 500;
    line-height: 1.7;
  }
  .feature-list li::before {
    content: "";
    width: 12px; height: 12px;
    background: var(--red-deep);
    transform: rotate(45deg);
    flex: none;
  }
  .suitable {
    margin-top: 42px;
    text-align: center;
    font-size: 13px;
  }
  .device-row {
    display: flex;
    gap: 12px;
    margin-top: 8px;
  }
  .device {
    flex: 1;
    text-align: center;
    font-size: 10px;
    line-height: 1.3;
  }
  .device__photo {
    height: 100px;
    background: linear-gradient(135deg, #ffffff 55%, var(--red-deep) 55%);
    margin-bottom: 6px;
  }
  .back-footer {
    display: flex;
    justify-content: space-between;
    align-items: flex-end;
    margin-top: 34px;
    font-size: 11px;
    line-height: 1.4;
  }
  .cert-mark {
    width: 30px; height: 22px;
    border: 2px solid var(--white);
    border-radius: 3px;
    margin-top: 18px;
  }
</style>
</head>
<body>

  <section class="panel panel--front" aria-label="Box front">
    <header class="hang-tab">
      <span class="hang-hole"></span>
      <div class="tab-brand">
        <span class="brand brand--small"><span class="brand__name">PUFFIRA</span><span class="brand__url">puffira.com.au</span></span>
        <span class="count-badge"><span class="count-badge__num">50</span><span class="count-badge__icon" role="img" aria-label="Mouthpiece outline icon"></span></span>
      </div>
    </header>
    <div class="body">
      <div class="front-title">
        <span class="brand brand--large"><span class="brand__name">PUFFIRA</span><span class="brand__url">puffira.com.au</span></span>
        <p class="product-label">Mouthpieces</p>
      </div>
      <div class="mouthpiece-art" role="img" aria-label="Red line drawing of a breathalyser mouthpiece"></div>
    </div>
    <footer class="pack-band">
      <svg viewBox="0 0 460 120" preserveAspectRatio="none" aria-hidden="true">
        <defs>
          <linearGradient id="bandFront" x1="0" x2="1">
            <stop offset="0" stop-color="#e8000f"/><stop offset="0.6" stop-color="#b0000c"/><stop offset="1" stop-color="#5a0006"/>
          </linearGradient>
        </defs>
        <polygon points="0,0 210,0 260,44 460,44 460,120 0,120" fill="#8a8a8a"/>
        <polygon points="0,6 206,6 256,50 460,50 460,120 0,120" fill="url(#bandFront)"/>
      </svg>
      <div class="pack-band__text"><span class="pack-band__num">50</span><span class="pack-band__word">Pack</span></div>
    </footer>
  </section>

  <section class="panel panel--back" aria-label="Box back">
    <header class="hang-tab">
      <span class="hang-hole"></span>
      <div class="tab-brand">
        <span class="brand brand--small"><span class="brand__name">PUFFIRA</span><span class="brand__url">puffira.com.au</span></span>
        <span class="count-badge"><span class="count-badge__num">50</span><span class="count-badge__icon" role="img" aria-label="Mouthpiece outline icon"></span></span>
      </div>
    </header>
    <div class="body">
      <div class="back-content">
        <h2 class="back-heading">50 PUFFIRA Mouthpieces</h2>
        <ul class="feature-list">
          <li>Premium Hygenic Plastic</li>
          <li>Disposable</li>
          <li>CE Approved</li>
        </ul>
        <p class="suitable">Suitable for</p>
        <div class="device-row">
          <div class="device">
            <div class="device__photo" role="img" aria-label="Photo of a yellow professional breathalyser"></div>
            Puffira<br>Professional Breathalyser
          </div>
          <div class="device">
            <div class="device__photo" role="img" aria-label="Photo of a black personal breathalyser"></div>
            Puffira<br>Personal Breathalyser
          </div>
        </div>
        <div class="back-footer">
          <div>
            PUFFIRA<br>Mouthpieces<br><br>Sample Address, Unit #<br>City, 12345
            <div class="cert-mark"></div>
          </div>
        </div>
      </div>
    </div>
    <footer class="pack-band">
      <svg viewBox="0 0 460 120" preserveAspectRatio="none" aria-hidden="true">
        <defs>
          <linearGradient id="bandBack" x1="0" x2="1">
            <stop offset="0" stop-color="#7a0008"/><stop offset="0.5" stop-color="#c0000d"/><stop offset="1" stop-color="#e8000f"/>
          </linearGradient>
        </defs>
        <polygon points="0,30 120,30 170,0 460,0 460,120 0,120" fill="#8a8a8a"/>
        <polygon points="0,36 124,36 174,6 460,6 460,120 0,120" fill="url(#bandBack)"/>
      </svg>
      <span class="pack-band__url">puffira.com.au</span>
    </footer>
  </section>

</body>
</html>
```